R&T Architects - business card and stationary

Aloha,

We have a simple text logo, we need it incorporated into a business card and also stationary design (letterhead) if possible.

Please check out our website, rtamaui-studio.example for a little more about us. The logo we would like to use is in the upper left corner of the website. It is a simple colored logo based on the Klavica font. We are open to new logo's as well, but we want simple.

Thanks

```html
<!DOCTYPE html>
<html lang="en">
<head>
<meta charset="utf-8">
<title>R&amp;T Architects – Stationery</title>
<link rel="stylesheet" href="https://fonts.googleapis.com/css2?family=Didact+Gothic&family=Libre+Franklin:ital,wght@0,400;1,400&display=swap">
<style>
  :root {
    --paper: #ffffff;
    --canvas: #ffffff;
    --brown: #5b4a2c;
    --brown-soft: #6a5a3e;
    --ink: #46483f;
    --green: #8cb43c;
    --tan: #c9b58f;
    --rule: #d8c9a8;
    --ghost: #f0f0e8;
    --edge: #bfb29a;
    --sig: #f1eee8;
  }
  * { box-sizing: border-box; margin: 0; padding: 0; }
  html, body { width: 1200px; height: 900px; overflow: hidden; background: var(--canvas); }
  body { position: relative; font-family: "Didact Gothic", sans-serif; color: var(--brown); }

  /* Letterhead */
  .letterhead {
    position: absolute; left: 55px; top: 68px; width: 613px; height: 800px;
    background: var(--paper); border: 1px solid var(--edge);
    box-shadow: 2px 3px 4px rgba(0,0,0,.25); overflow: hidden;
  }
  .letterhead__header { position: absolute; left: 24px; right: 22px; top: 24px; font-size: 10.5px; line-height: 12px; }
  .contact { position: absolute; top: 0; width: 220px; }
  .contact--right { right: 0; text-align: right; }
  .contact__divider { width: 110px; border-top: 1px dashed var(--rule); margin: 7px 0 6px; }
  .contact--right .contact__divider { margin-left: auto; }
  .contact__name { color: var(--green); }
  .contact__role { color: var(--tan); font-size: 8.5px; line-height: 10px; }
  .contact__email { margin-top: 8px; }
  .contact__phone { color: var(--tan); margin-top: 6px; }
  .letterhead__rule { position: absolute; left: 24px; right: 22px; top: 137px; border-top: 1px dashed var(--rule); }

  .letter__salutation { position: absolute; left: 24px; top: 162px; font-size: 12.5px; }
  .letter__body {
    position: absolute; left: 63px; top: 190px; width: 484px;
    font-family: "Libre Franklin", sans-serif; font-style: italic; font-weight: 400;
    font-size: 10.1px; line-height: 12.3px; color: var(--brown-soft);
  }
  .letter__body p { margin-bottom: 12px; }
  .letter__closing { position: absolute; right: 22px; top: 630px; font-size: 12px; }
  .letter__signature { position: absolute; right: 46px; top: 656px; width: 44px; height: 42px; }
  .letterhead__ghost-name {
    position: absolute; left: 0; bottom: -10px; white-space: nowrap;
    font-family: "Libre Franklin", sans-serif; font-weight: 400;
    font-size: 96px; line-height: 1; color: var(--ghost);
  }

  /* Wordmark */
  .wordmark {
    position: absolute; left: 740px; top: 104px;
    font-family: "Libre Franklin", sans-serif; font-weight: 400;
    font-size: 50px; line-height: 1; color: var(--ink);
    display: flex; align-items: center; gap: 14px;
  }
  .wordmark__square { width: 14px; height: 14px; background: var(--green); }

  /* Business card */
  .card {
    position: absolute; left: 735px; top: 580px; width: 420px; height: 240px;
    background: var(--paper); border: 1px solid #e2ded5;
    box-shadow: 2px 3px 6px rgba(0,0,0,.18); font-size: 10px; line-height: 12px;
  }
  .card__person { position: absolute; right: 22px; top: 20px; text-align: right; }
  .card__name { color: var(--green); font-size: 13px; line-height: 14px; }
  .card__role { color: var(--tan); font-size: 9px; }
  .card__email { position: absolute; right: 22px; top: 60px; font-size: 12.5px; }
  .card__phone { position: absolute; right: 22px; top: 76px; font-size: 12.5px; color: var(--tan); }
  .card__brand {
    position: absolute; left: 22px; top: 104px;
    font-family: "Libre Franklin", sans-serif; font-weight: 400;
    font-size: 26px; line-height: 1; color: var(--ink);
  }
  .card__tagline { position: absolute; left: 22px; top: 140px; width: 250px; font-size: 7.5px; line-height: 9px; color: var(--brown-soft); }
  .card__web { position: absolute; left: 22px; top: 164px; color: var(--tan); font-size: 10px; }
  .card__rule { position: absolute; left: 22px; right: 22px; top: 184px; border-top: 1px dashed var(--rule); }
  .card__address { position: absolute; top: 192px; font-size: 8px; line-height: 10px; }
  .card__address--office { left: 22px; }
  .card__address--mailing { right: 22px; text-align: right; }
  .card__label { color: var(--tan); }
</style>
</head>
<body>

<section class="letterhead" aria-label="Letterhead">
  <header class="letterhead__header">
    <div class="contact contact--left">
      <div>office:</div>
      <div>48-210 Palila Road</div>
      <div>Honokaa, Hawaii 96799</div>
      <div class="contact__divider"></div>
      <div class="contact__name">Sam Kealoha</div>
      <div class="contact__role">Architect</div>
      <div class="contact__email">sam@rtamaui-studio.example</div>
      <div class="contact__phone">808.555.0142</div>
    </div>
    <div class="contact contact--right">
      <div>mailing:</div>
      <div>48-210 Nene Place</div>
      <div>Honokaa, Hawaii 96799</div>
      <div class="contact__divider"></div>
      <div class="contact__name">Kai Lindqvist</div>
      <div class="contact__role">Architect</div>
      <div class="contact__email">kai@rtamaui-studio.example</div>
      <div class="contact__phone">808.555.0178</div>
    </div>
  </header>
  <div class="letterhead__rule"></div>

  <p class="letter__salutation">Client,</p>
  <div class="letter__body">
    <p>Suspendisse lacus nunc, porttitor sit amet interdum eu, fringilla a quam. Donec vel nunc non leo tempor cursus. Donec euismod pretium eros eu hendrerit. Sed risus nibh, gravida eu venenatis at, placerat non diam. Suspendisse accumsan, dolor vel malesuada accumsan, diam magna aliquam arcu, non euismod urna urna congue metus. Mauris euismod blandit volutpat. Pellentesque habitant morbi tristique senectus et netus et malesuada fames ac turpis egestas. Praesent id velit enim. Pellentesque gravida auctor neque eu elementum. Cras molestie, felis at blandit feugiat, dui lacus sodales lacus, in aliquam nulla est at lectus. Etiam id pharetra sem. Vestibulum eu dui sit amet mi posuere dapibus. Etiam gravida mi quis mi pretium vulputate. Sed non ultricies urna.</p>
    <p>Aliquam lacinia justo ac diam auctor in porta urna interdum. Nullam vel neque cursus leo accumsan sodales in ac nisl. Suspendisse porta hendrerit velit quis posuere. Cras mattis interdum dolor vitae venenatis. Nam porta turpis eros. Donec imperdiet nibh id orci commodo at dapibus orci vestibulum. Donec id tellus nisl. Morbi ut tortor felis. Quisque fringilla mauris ultrices sapien vestibulum quis mattis massa interdum. Nullam nisi nulla, egestas vel vehicula nec, adipiscing eu purus. Etiam a sodales libero. Etiam porta leo dolor, eu vestibulum arcu. Mauris rhoncus ornare libero, non feugiat magna malesuada at. Praesent nec dolor lectus. Donec tincidunt nunc ut tortor aliquam ullamcorper. Nulla suscipit condimentum fermentum. Maecenas vel odio massa, ut dapibus nisl. Praesent et consectetur nulla. In pretium sapien non turpis porttitor fermentum.</p>
    <p>Integer sodales urna a magna commodo tempus. Nunc a enim mauris. Pellentesque a velit sit amet nulla lacinia feugiat id vel lectus. Aliquam scelerisque elementum felis, eget semper ante ornare ac. Aenean eros tellus, tristique tristique porttitor quis, ornare id mauris. Aliquam pulvinar lacus tellus, vel pretium nisl. Sed hendrerit tortor est, vel rhoncus ipsum. Lorem ipsum dolor sit amet, consectetur adipiscing elit. Phasellus congue euismod metus, nec blandit nisl adipiscing id. Quisque in ante ac libero iaculis venenatis. Nullam eget justo purus. Nam at sapien justo, vel dignissim nisi. Aenean sit amet tempus metus. Proin egestas, justo non elementum facilisis, turpis erat feugiat enim, ac sollicitudin odio mauris at leo. Quisque pharetra, nisl tempor convallis lobortis, leo lacus auctor quam, at commodo nisl tortor accumsan turpis. Fusce in neque vel ipsum semper pharetra.</p>
    <p>sed eu sapien. Cras at consequat nibh. Etiam in vulputate sapien. Donec consequat placerat massa sed pharetra. Suspendisse neque augue, viverra a eleifend at, tempus vel enim. Nunc semper, eros a consectetur vestibulum, tellus dui dictum elit, vitae pellentesque ligula nisi at nulla. Curabitur eu est odio, malesuada iaculis tellus.</p>
  </div>
  <p class="letter__closing">Sincerely</p>
  <svg class="letter__signature" role="img" aria-label="Handwritten signature" viewBox="0 0 44 42">
    <rect width="44" height="42" rx="5" fill="var(--sig)"/>
  </svg>
  <div class="letterhead__ghost-name" aria-hidden="true">R&amp;T Architects</div>
</section>

<div class="wordmark">
  <span class="wordmark__square"></span>
  <span>R&amp;T Architects</span>
</div>

<section class="card" aria-label="Business card">
  <div class="card__person">
    <div class="card__name">Sam Kealoha</div>
    <div class="card__role">Architect</div>
  </div>
  <div class="card__email">sam@rtamaui-studio.example</div>
  <div class="card__phone">808.555.0142</div>
  <div class="card__brand">R&amp;T Architects</div>
  <p class="card__tagline">Full service architecture studio focused on sustainable, low energy island homes and workplaces.</p>
  <div class="card__web">www.rtamaui-studio.example</div>
  <div class="card__rule"></div>
  <div class="card__address card__address--office">
    <div class="card__label">office:</div>
    <div>48-210 Palila Road</div>
    <div>Honokaa, Hawaii 96799</div>
  </div>
  <div class="card__address card__address--mailing">
    <div class="card__label">mailing:</div>
    <div>48-210 Nene Place</div>
    <div>Honokaa, Hawaii 96799</div>
  </div>
</section>

</body>
</html>
```